Fire Risk Assessment App needs a sleek UI design

I need a sleek, modern but professional design for my 5 page Fire Risk Assessment App. Include gradient background, fire themed colours including reds, yellows, light orange and a touch of black. Design must ooze simplicity and professionalism. This is for the UK market. See attached images and word doc for more information.

Target Market(s)

General public and business owners

Industry/Entity Type

Technology / Fire Safety

Colors
00AB8E
00BBA5
67D7C9
C6EFE9
E9F9F6
59FF00
82FF00
B8FF75
E3FFCB
F4FFEA
FFC000
F8CF3A
FAE287
FDF2CF
FEFAEE
F0912C
F2A743
F7CA91
FBE8D2
FDF5EE
EE7325
F08F49
F5BC92
FAE3D3
FDF4ED
EB3D1F
EC4F4E
F09395
F8D3D4
FCEDEE

```html
<!DOCTYPE html>
<html lang="en">
<head>
<meta charset="utf-8">
<title>Fire Risk Assessment – App Screens</title>
<link rel="stylesheet" href="https://fonts.googleapis.com/css2?family=Poppins:wght@400;500;600;700;800&display=swap">
<style>
:root{
  --bg:#3a1313;
  --bg-deep:#2a0d0d;
  --red:#eb3d1f;
  --red-deep:#c92a1a;
  --red-dark:#b3231a;
  --orange:#ee7325;
  --orange-soft:#f08f49;
  --amber:#ffc000;
  --yellow:#f8cf3a;
  --peach:#fae3d3;
  --pink-soft:#fcedee;
  --green:#35b24a;
  --white:#ffffff;
  --ink:#1d1d1d;
  --grey:#8a8a8a;
  --line:#ececec;
}
*{box-sizing:border-box;margin:0;padding:0}
html,body{width:1200px;height:1200px;overflow:hidden;background:var(--bg)}
body{font-family:"Poppins",sans-serif;color:var(--white)}
.board{position:absolute;left:0;top:0;width:1932px;height:1932px;transform:scale(.62112);transform-origin:0 0;
  background:radial-gradient(ellipse at 70% 20%,#4a1818 0%,var(--bg) 50%,var(--bg-deep) 100%)}
.brand{position:absolute;left:678px;top:105px;display:flex;align-items:center;gap:32px}
.brand-mark{width:66px;height:66px;border-radius:50%;background:var(--orange)}
.brand-name{font-weight:800;font-size:50px;letter-spacing:-.5px;color:var(--white)}

.label{position:absolute;transform-origin:0 0;transform:rotate(-90deg);font-size:6.5px;letter-spacing:4px;color:rgba(255,255,255,.8);white-space:nowrap;font-weight:500}

.screen{position:absolute;width:146px;height:318px;border-radius:18px;overflow:hidden;background:var(--red);font-size:5px}
.screen.tall{height:494px}
.abs{position:absolute}
.status{position:absolute;top:7px;left:14px;right:14px;display:flex;justify-content:space-between;font-size:5px;font-weight:600}
.status i{display:inline-block;width:4px;height:3px;background:currentColor;margin-left:2px;border-radius:1px}
.home-bar{position:absolute;bottom:5px;left:50%;width:44px;height:2px;margin-left:-22px;border-radius:2px;background:rgba(255,255,255,.85)}
.home-bar.dark{background:#222}

.grad-splash{background:linear-gradient(180deg,#f6b431 0%,#f08a2c 45%,#eb3d1f 100%)}
.grad-red{background:linear-gradient(180deg,#e2361e 0%,#c92a1a 100%)}

.splash-mark{position:absolute;left:57px;top:72px;width:32px;height:32px;border-radius:50%;background:var(--white)}
.splash-name{position:absolute;left:0;right:0;top:110px;text-align:center;font-weight:700;font-size:8px}
.splash-sub{position:absolute;left:0;right:0;text-align:center;font-size:3.6px;color:rgba(255,255,255,.85)}
.glow{position:absolute;left:20px;right:20px;top:190px;height:110px;border-radius:50% 50% 10px 10px;background:radial-gradient(ellipse at 50% 80%,rgba(255,255,255,.18),rgba(255,255,255,0) 70%)}

.auth-card{position:absolute;left:10px;right:10px;top:255px;height:46px;background:var(--white);border-radius:6px;color:var(--ink);padding:8px 7px}
.auth-card p{font-size:4.2px;margin-bottom:6px}
.btn-row{display:flex;gap:6px}
.pill{flex:1;height:12px;border-radius:7px;display:flex;align-items:center;justify-content:center;font-size:4.2px;font-weight:600}
.pill.solid{background:var(--red);color:var(--white)}
.pill.line{border:1px solid var(--red);color:var(--red);background:var(--white)}
.pill.ghost{border:1px solid var(--white);color:var(--white)}
.pill.light{background:var(--white);color:var(--red)}

.illustration{position:absolute;left:16px;right:16px;top:30px;height:180px;border-radius:6px;
  background:linear-gradient(160deg,rgba(255,255,255,.75) 0%,rgba(255,255,255,.35) 45%,rgba(235,61,31,.55) 100%)}
.walk-text{position:absolute;left:10px;right:10px;top:232px;font-size:6px;line-height:1.35}
.walk-text b{font-weight:700}
.walk-note{position:absolute;left:10px;top:262px;font-size:3.8px;color:rgba(255,255,255,.9)}
.dots{position:absolute;left:12px;top:288px;display:flex;gap:2px}
.dots i{display:block;width:4px;height:1.6px;border-radius:1px;background:rgba(255,255,255,.5)}
.dots i.on{width:7px;background:var(--white)}
.next-fab{position:absolute;right:12px;top:282px;width:14px;height:14px;border-radius:50%;background:var(--white);color:var(--red);font-size:7px;display:flex;align-items:center;justify-content:center;font-weight:700}

.app-head{position:absolute;left:8px;right:8px;top:24px;display:flex;align-items:center;gap:4px;font-size:7px;font-weight:700}
.app-head .dot{width:8px;height:8px;border-radius:50%;background:var(--white)}
.app-head .profile{margin-left:auto;width:8px;height:8px;border-radius:50%;background:var(--white)}

.card{position:absolute;left:8px;right:8px;background:var(--white);border-radius:5px;color:var(--ink);padding:6px}
.card-head{display:flex;justify-content:space-between;font-size:4.2px;font-weight:600}
.card-head span{color:var(--red);font-size:3.6px}
.item{display:flex;align-items:center;gap:4px;margin-top:5px;padding:4px;border:1px solid var(--line);border-radius:3px}
.item .ico{width:9px;height:9px;border-radius:2px;background:var(--red-deep);flex:none}
.item b{display:block;font-size:4.2px;font-weight:600}
.item small{display:block;font-size:3.2px;color:var(--grey)}
.tag{display:inline-block;margin-top:1px;padding:0 3px;border-radius:3px;font-size:2.8px;font-weight:600}
.tag.progress{background:var(--peach);color:var(--orange)}
.tag.done{background:#dff3e3;color:var(--green)}
.ring{margin-left:auto;width:10px;height:10px;border-radius:50%;border:1.4px solid var(--green);font-size:2.8px;display:flex;align-items:center;justify-content:center;color:var(--ink);font-weight:700}
.chev{margin-left:auto;font-size:5px;color:var(--grey)}
.slide-dots{display:flex;justify-content:center;gap:2px;margin:5px 0}
.slide-dots i{width:2px;height:1.4px;background:#ddd}
.slide-dots i.on{width:8px;background:var(--red)}
.add-btn{height:10px;border-radius:6px;background:var(--red);color:var(--white);font-size:4px;font-weight:600;display:flex;align-items:center;justify-content:center}
.empty{text-align:center;font-size:3.6px;color:var(--grey);padding:10px 0 6px}
.warn{width:0;height:0;margin:0 auto 4px;border-left:4px solid transparent;border-right:4px solid transparent;border-bottom:7px solid var(--red)}

.section-title{position:absolute;left:8px;font-size:5.6px;font-weight:600}
.row{position:absolute;left:8px;right:8px;height:22px;background:var(--white);border-radius:3px;color:var(--ink);display:flex;align-items:center;gap:4px;padding:0 5px}
.row .ico{width:8px;height:8px;background:var(--red-deep);border-radius:1px}
.row b{display:block;font-size:4px;font-weight:600}
.row small{display:block;font-size:3px;color:var(--grey)}
.tick{margin-left:auto;width:10px;height:10px;border-radius:50%;border:1px solid var(--green);color:var(--green);font-size:5px;display:flex;align-items:center;justify-content:center}
.view-all{position:absolute;left:44px;width:58px;height:9px;border-radius:5px;border:1px solid var(--white);color:var(--white);font-size:3.4px;font-weight:600;display:flex;align-items:center;justify-content:center}
.purchase{position:absolute;left:8px;right:8px;display:flex;gap:4px;align-items:flex-start}
.purchase .ico{width:8px;height:8px;border-radius:50%;background:var(--white);flex:none}
.purchase b{display:block;font-size:3.8px;font-weight:600}
.purchase small{display:block;font-size:3px;opacity:.8}

.tabbar{position:absolute;left:0;right:0;bottom:0;height:36px;background:var(--white);display:flex;justify-content:space-around;padding:6px 6px 0;color:#b5b5b5}
.tab{display:flex;flex-direction:column;align-items:center;font-size:2.6px;gap:1px}
.tab i{width:7px;height:7px;border-radius:2px;border:1px solid currentColor}
.tab.on{color:var(--red)}
.tab.on i{background:var(--red);border-color:var(--red);border-radius:50%}
.tab.fire i{width:9px;height:9px;border-radius:50%;background:var(--orange);border:none}

.light-bottom{position:absolute;left:0;right:0;top:124px;bottom:0;background:var(--white);color:var(--ink)}
.light-bottom .section-title{color:var(--ink)}
.light-bottom .row{border:none;background:transparent}
.light-bottom .view-all{border-color:var(--red);color:var(--red)}
.light-bottom .purchase .ico{background:var(--red-deep);border-radius:1px}

.lead{position:absolute;left:8px;font-size:4.2px;font-weight:500}
.option{position:absolute;left:8px;right:8px;height:21px;border:1px solid rgba(255,255,255,.85);border-radius:4px;padding:3px 5px}
.option .plan{display:inline-block;background:var(--white);color:var(--red);font-size:2.8px;font-weight:700;padding:0 3px;border-radius:2px}
.option .price{display:block;font-size:5px;font-weight:700;margin-top:1px}
.option .badge{position:absolute;right:14px;top:-4px;background:var(--white);color:var(--red);font-size:2.6px;font-weight:700;padding:0 5px;border-radius:3px}
.option.best{background:var(--white);color:var(--red)}
.option.best .plan{background:var(--red);color:var(--white)}
.option.best .badge{background:var(--amber);color:var(--ink)}
.option .check{position:absolute;right:5px;top:7px;width:6px;height:6px;border-radius:50%;background:var(--red)}
.actions{position:absolute;left:8px;right:8px;display:flex;gap:8px}

.textarea{position:absolute;left:8px;right:8px;top:64px;height:128px;border-radius:5px;background:rgba(120,20,12,.55);padding:5px;font-size:3.4px;color:rgba(255,255,255,.75)}
.mic-dot{position:absolute;right:5px;top:4px;width:8px;height:8px;border-radius:50%;background:var(--white)}

.choice{position:absolute;left:8px;right:8px;height:18px;border-radius:10px;display:flex;align-items:center;padding:0 5px;gap:4px;font-size:4.2px;font-weight:600;border:1px solid var(--white);color:var(--white)}
.choice .ico{width:8px;height:8px;border-radius:50%;border:1px solid currentColor}
.choice.sel{background:var(--white);color:var(--red)}
.choice .check{margin-left:auto;width:7px;height:7px;border-radius:50%;background:var(--red)}

.q-head{position:absolute;left:0;right:0;top:0;height:66px;background:linear-gradient(180deg,#e2361e,#d22e1c)}
.q-kicker{position:absolute;left:8px;top:27px;font-size:3px;font-weight:600;opacity:.9}
.q-title{position:absolute;left:8px;top:33px;font-size:8px;font-weight:700}
.q-section{position:absolute;left:8px;top:48px;font-size:4.4px}
.q-section b{font-weight:700}
.q-save{position:absolute;right:8px;top:25px;text-align:center;font-size:3px}
.q-save i{display:block;width:9px;height:9px;margin:0 auto 2px;border-radius:50%;background:var(--white)}
.q-body{position:absolute;left:0;right:0;top:66px;bottom:0;background:var(--white);color:var(--ink)}
.badge-ico{position:absolute;left:61px;top:-10px;width:24px;height:24px;border-radius:50%;background:var(--white);border:1.6px solid var(--green);display:flex;align-items:center;justify-content:center}
.center-t{position:absolute;left:0;right:0;text-align:center}
.q-topic{font-size:4.6px;font-weight:600}
.q-clause{font-size:3.6px;color:var(--grey)}
.q-num{position:absolute;left:8px;font-size:3.2px;font-weight:700;color:var(--red)}
.q-text{position:absolute;left:8px;right:8px;font-size:6px;font-weight:600;line-height:1.4}
.answers{position:absolute;left:18px;right:18px;display:flex;justify-content:space-between}
.ans{display:flex;flex-direction:column;align-items:center;gap:2px;font-size:3px;color:var(--ink)}
.ans i{width:12px;height:12px;border-radius:50%;border:1.2px solid;display:flex;align-items:center;justify-content:center;font-style:normal;font-size:6px;font-weight:700}
.ans.no i{border-color:var(--red);color:var(--red)}
.ans.na i{border-color:var(--orange);color:var(--orange)}
.ans.yes i{border-color:var(--green);color:var(--green)}
.ans.no.sel i{background:var(--red);color:var(--white)}
.ans.yes.sel i{background:var(--green);color:var(--white)}
.ans.sel{font-weight:700}
.ans.no.sel{color:var(--red)}
.ans.yes.sel{color:var(--green)}
.comment{position:absolute;left:8px;right:8px;height:14px;border:1px solid var(--line);border-radius:3px;font-size:3.4px;font-weight:500;padding:0 5px;display:flex;align-items:center}
.mini{position:absolute;left:8px;font-size:2.8px;color:var(--grey);letter-spacing:.2px}
.tools{position:absolute;left:8px;right:8px;display:flex;gap:6px}
.tool{flex:1;height:10px;border-radius:3px;background:var(--pink-soft);font-size:3.6px;display:flex;align-items:center;padding-left:5px;gap:3px}
.tool i{width:3px;height:4px;background:var(--ink);border-radius:1px}
.progress{position:absolute;left:8px;right:8px}
.progress .meta{display:flex;justify-content:space-between;font-size:2.6px;color:var(--ink)}
.progress .bar{margin-top:2px;height:2px;border-radius:1px;background:#e6e6e6}
.progress .bar i{display:block;width:60%;height:100%;border-radius:1px;background:var(--green)}
.nav{position:absolute;left:8px;right:8px;display:flex;gap:10px}
.nav .pill{height:11px}
.photo{position:absolute;left:8px;right:8px;top:210px;height:130px;border-radius:4px;
  background:linear-gradient(150deg,#9a9ea2 0%,#5c6064 50%,#8a8e91 100%)}
.photo .remove{position:absolute;right:4px;top:4px;width:8px;height:8px;border-radius:50%;background:var(--white)}
</style>
</head>
<body>
<main class="board">

  <header class="brand">
    <span class="brand-mark"></span>
    <h1 class="brand-name">Fire Risk Assessment</h1>
  </header>

  <!-- Row 1 -->
  <span class="label" style="left:549px;top:432px">SPLASH SCREEN V1</span>
  <section class="screen grad-splash" style="left:568px;top:302px">
    <div class="status"><span>9:41</span><span><i></i><i></i><i></i></span></div>
    <span class="splash-mark"></span>
    <p class="splash-name">Fire Risk Assessment</p>
    <div class="glow" role="img" aria-label="Soft flame glow"></div>
    <p class="splash-sub" style="top:294px">Created and endorsed by UK Fire Safety Professionals</p>
    <span class="home-bar"></span>
  </section>

  <span class="label" style="left:772px;top:432px">SPLASH SCREEN V2</span>
  <section class="screen grad-splash" style="left:791px;top:302px">
    <div class="status"><span>9:41</span><span><i></i><i></i><i></i></span></div>
    <span class="splash-mark"></span>
    <p class="splash-name">Fire Risk Assessment</p>
    <p class="splash-sub" style="top:124px">Created and endorsed by UK Fire Safety Professionals</p>
    <div class="glow" role="img" aria-label="Soft flame glow"></div>
    <div class="auth-card">
      <p>Any responsible person can do it</p>
      <div class="btn-row"><span class="pill line">Sign up</span><span class="pill solid">Sign in</span></div>
    </div>
    <span class="home-bar"></span>
  </section>

  <span class="label" style="left:995px;top:482px">WALKTHROUGH SCREEN V1</span>
  <section class="screen grad-splash" style="left:1014px;top:302px">
    <div class="status"><span>9:41</span><span><i></i><i></i><i></i></span></div>
    <div class="illustration" role="img" aria-label="Illustration of assessment report pages with a tapping hand"></div>
    <p class="walk-text">The most user friendly<br><b>Fire Risk Assessment</b> available</p>
    <p class="walk-note">Quick tap responses and voice activated typing.</p>
    <div class="dots"><i class="on"></i><i></i><i></i></div>
    <span class="next-fab">→</span>
    <span class="home-bar"></span>
  </section>

  <span class="label" style="left:1218px;top:482px">WALKTHROUGH SCREEN V2</span>
  <section class="screen grad-splash" style="left:1237px;top:302px">
    <div class="status"><span>9:41</span><span><i></i><i></i><i></i></span></div>
    <div class="illustration" role="img" aria-label="Illustration of a fire hazards question card with a tapping hand"></div>
    <p class="walk-text">The most user friendly<br><b>Fire Risk Assessment</b> available</p>
    <p class="walk-note">Quick tap responses and voice activated typing.</p>
    <div class="dots"><i></i><i class="on"></i><i></i></div>
    <span class="next-fab">→</span>
    <span class="home-bar"></span>
  </section>

  <!-- Row 2 -->
  <span class="label" style="left:549px;top:876px">DASHBOARD DESIGN ALT 1</span>
  <section class="screen grad-red" style="left:568px;top:694px">
    <div class="status"><span>9:41</span><span><i></i><i></i><i></i></span></div>
    <div class="app-head"><span class="dot"></span>Dashboard<span class="profile"></span></div>
    <div class="card" style="top:42px">
      <div class="card-head">Fire Risk Assessments<span>VIEW ALL</span></div>
      <div class="item"><span class="ico"></span><div><b>Hartley Residence</b><small>Section 7.01 / 30.00</small><span class="tag progress">IN PROGRESS</span></div><span class="chev">›</span></div>
      <div class="slide-dots"><i class="on"></i><i></i><i></i><i></i></div>
      <div class="add-btn">Add new assessment</div>
    </div>
    <p class="section-title" style="top:138px">Completed Assessments</p>
    <div class="row" style="top:152px"><span class="ico"></span><div><b>Elmwood Care Home</b><span class="tag done">COMPLETED</span></div><span class="chev">›</span></div>
    <div class="row" style="top:180px"><span class="ico"></span><div><b>The Willow Residences</b><span class="tag done">COMPLETED</span></div><span class="chev">›</span></div>
    <span class="view-all" style="top:212px">View all completed →</span>
    <p class="section-title" style="top:237px">Purchase History</p>
    <div class="purchase" style="top:250px"><span class="ico"></span><div><b>Residential Fire Risk Assessments</b><small>Sun, 12 July 2024 • 16:20:32</small></div></div>
    <div class="purchase" style="top:273px"><span class="ico"></span><div><b>Commercial Fire Risk Assessments</b></div></div>
    <nav class="tabbar"><span class="tab on"><i></i>Dashboard</span><span class="tab"><i></i>Purchases</span><span class="tab fire"><i></i></span><span class="tab"><i></i>Support</span><span class="tab"><i></i>Logout</span></nav>
    <span class="home-bar dark"></span>
  </section>

  <span class="label" style="left:772px;top:884px">DASHBOARD DESIGN ALT 2A</span>
  <section class="screen grad-red" style="left:791px;top:694px">
    <div class="status"><span>9:41</span><span><i></i><i></i><i></i></span></div>
    <div class="app-head"><span class="dot"></span>Dashboard<span class="profile"></span></div>
    <div class="card" style="top:42px">
      <div class="card-head">Fire Risk Assessments<span>VIEW ALL</span></div>
      <div class="item"><span class="ico"></span><div><b>Hartley Residence</b><span class="tag progress">IN PROGRESS</span></div><span class="ring">75%</span></div>
      <div class="slide-dots"><i class="on"></i><i></i><i></i><i></i></div>
      <div class="add-btn">Add new assessment</div>
    </div>
    <p class="section-title" style="top:138px">Completed Assessments</p>
    <div class="row" style="top:152px"><span class="ico"></span><div><b>Elmwood Care Home</b><small>18 Jul 2024</small></div><span class="tick">✓</span></div>
    <div class="row" style="top:180px"><span class="ico"></span><div><b>The Willow Residences</b><small>18 Jul 2024</small></div><span class="tick">✓</span></div>
    <span class="view-all" style="top:212px">View all completed →</span>
    <p class="section-title" style="top:240px">Purchase History</p>
    <div class="purchase" style="top:254px"><span class="ico"></span><div><b>Residential Fire Risk Assessments</b><small>Sun, 12 July 2024 • 16:20:32</small></div></div>
    <div class="purchase" style="top:276px"><span class="ico"></span><div><b>Commercial Fire Risk Assessments</b></div></div>
    <nav class="tabbar"><span class="tab on"><i></i>Dashboard</span><span class="tab"><i></i>Purchases</span><span class="tab fire"><i></i></span><span class="tab"><i></i>Support</span><span class="tab"><i></i>Logout</span></nav>
    <span class="home-bar dark"></span>
  </section>

  <span class="label" style="left:995px;top:884px">DASHBOARD DESIGN ALT 2B</span>
  <section class="screen grad-red" style="left:1014px;top:694px">
    <div class="status"><span>9:41</span><span><i></i><i></i><i></i></span></div>
    <div class="app-head"><span class="dot"></span>Dashboard<span class="profile"></span></div>
    <div class="card" style="top:42px">
      <div class="card-head">Fire Risk Assessments</div>
      <div class="empty"><div class="warn"></div>No current assessments!</div>
      <div class="add-btn" style="margin-top:6px">Add new assessment</div>
    </div>
    <p class="section-title" style="top:138px">Completed Assessments</p>
    <div class="row" style="top:152px"><span class="ico"></span><div><b>Elmwood Care Home</b><small>18 Jul 2024</small></div><span class="tick">✓</span></div>
    <div class="row" style="top:180px"><span class="ico"></span><div><b>The Willow Residences</b><small>18 Jul 2024</small></div><span class="tick">✓</span></div>
    <span class="view-all" style="top:212px">View all completed →</span>
    <p class="section-title" style="top:240px">Purchase History</p>
    <div class="purchase" style="top:254px"><span class="ico"></span><div><b>Residential Fire Risk Assessments</b><small>Sun, 12 July 2024 • 16:20:32</small></div></div>
    <div class="purchase" style="top:276px"><span class="ico"></span><div><b>Commercial Fire Risk Assessments</b></div></div>
    <nav class="tabbar"><span class="tab on"><i></i>Dashboard</span><span class="tab"><i></i>Purchases</span><span class="tab fire"><i></i></span><span class="tab"><i></i>Support</span><span class="tab"><i></i>Logout</span></nav>
    <span class="home-bar dark"></span>
  </section>

  <span class="label" style="left:1218px;top:876px">DASHBOARD DESIGN ALT 3</span>
  <section class="screen grad-red" style="left:1237px;top:694px">
    <div class="status"><span>9:41</span><span><i></i><i></i><i></i></span></div>
    <div class="app-head" style="top:22px"><span class="dot"></span>Dashboard<span class="profile"></span></div>
    <div class="card" style="top:40px">
      <div class="card-head">Fire Risk Assessments<span>VIEW ALL</span></div>
      <div class="item"><span class="ico" style="background:var(--orange)"></span><div><b>Hartley Residence</b><span class="tag progress">IN PROGRESS</span></div><span class="ring">75%</span></div>
      <div class="slide-dots"><i class="on"></i><i></i><i></i><i></i></div>
      <div class="add-btn">Add new assessment</div>
    </div>
    <div class="light-bottom">
      <p class="section-title" style="top:6px">Completed Assessments</p>
      <div class="row" style="top:18px"><span class="ico"></span><div><b>Elmwood Care Home</b><small>18 Jul 2024</small></div><span class="tick">✓</span></div>
      <div class="row" style="top:46px"><span class="ico" style="background:var(--orange)"></span><div><b>The Willow Residences</b><small>18 Jul 2024</small></div><span class="tick">✓</span></div>
      <span class="view-all" style="top:76px">View all completed →</span>
      <p class="section-title" style="top:104px">Purchase History</p>
      <div class="purchase" style="top:118px"><span class="ico" style="background:var(--orange)"></span><div><b>Residential Fire Risk Assessments</b><small>Sun, 12 July 2024 • 16:20:32</small></div></div>
      <div class="purchase" style="top:140px"><span class="ico"></span><div><b>Commercial Fire Risk Assessments</b><small>Sun, 5 July 2024 • 10:45:12</small></div></div>
    </div>
    <nav class="tabbar" style="border-top:1px solid var(--red)"><span class="tab on"><i></i>Dashboard</span><span class="tab"><i></i>Purchases</span><span class="tab fire"><i></i></span><span class="tab"><i></i>Support</span><span class="tab"><i></i>Logout</span></nav>
    <span class="home-bar dark"></span>
  </section>

  <!-- Row 3 -->
  <span class="label" style="left:549px;top:1220px">PURCHASE OPTIONS</span>
  <section class="screen grad-red" style="left:568px;top:1086px">
    <div class="status"><span>9:41</span><span><i></i><i></i><i></i></span></div>
    <div class="app-head"><span class="dot" style="border-radius:1px"></span>Purchase Options</div>
    <p class="lead" style="top:60px">Fire Risk Assessment Payment Options</p>
    <div class="option" style="top:78px"><span class="plan">BRONZE 1</span><span class="price">£19.99</span></div>
    <div class="option best" style="top:108px"><span class="badge">BEST PRICE</span><span class="plan">SILVER 3</span><span class="price">£54.99</span><span class="check"></span></div>
    <div class="option" style="top:140px"><span class="badge">SAVE 20%</span><span class="plan">GOLD 5</span><span class="price">£89.99</span></div>
    <div class="option" style="top:170px"><span class="badge">SAVE 30%</span><span class="plan">PLATINUM 10</span><span class="price">£174.99</span></div>
    <div class="actions" style="top:261px"><span class="pill ghost">✕ Cancel</span><span class="pill light">Continue →</span></div>
    <nav class="tabbar" style="height:30px"><span class="tab"><i></i>Dashboard</span><span class="tab on"><i></i>Purchases</span><span class="tab fire"><i></i></span><span class="tab"><i></i>Support</span><span class="tab"><i></i>Logout</span></nav>
    <span class="home-bar dark"></span>
  </section>

  <span class="label" style="left:772px;top:1202px">SUPPORT SCREEN</span>
  <section class="screen grad-red" style="left:791px;top:1086px">
    <div class="status"><span>9:41</span><span><i></i><i></i><i></i></span></div>
    <div class="app-head"><span class="dot"></span>Technical Support</div>
    <p class="lead" style="top:46px">Our email support is open 24/7.</p>
    <div class="textarea">Type or record your concerns here<span class="mic-dot"></span></div>
    <div class="actions" style="top:200px"><span class="pill ghost">➤ Send</span></div>
    <nav class="tabbar" style="height:30px"><span class="tab"><i></i>Dashboard</span><span class="tab"><i></i>Purchases</span><span class="tab fire"><i></i></span><span class="tab on"><i></i>Support</span><span class="tab"><i></i>Logout</span></nav>
    <span class="home-bar dark"></span>
  </section>

  <span class="label" style="left:995px;top:1240px">ADD NEW ASSESSMENT</span>
  <section class="screen grad-red" style="left:1014px;top:1086px">
    <div class="status"><span>9:41</span><span><i></i><i></i><i></i></span></div>
    <div class="app-head"><span class="dot"></span>Add Fire Risk Assessment</div>
    <p class="lead" style="top:60px">Select type of property</p>
    <div class="choice" style="top:78px"><span class="ico"></span>Residential</div>
    <div class="choice sel" style="top:108px"><span class="ico"></span>Commercial<span class="check"></span></div>
    <div class="actions" style="top:276px"><span class="pill ghost">✕ Cancel</span><span class="pill light">Continue →</span></div>
    <span class="home-bar"></span>
  </section>

  <span class="label" style="left:1218px;top:1390px">ADD ASSESSMENT - QUESTION - ADD PHOTO</span>
  <section class="screen tall" style="left:1237px;top:1086px">
    <div class="status"><span>9:41</span><span><i></i><i></i><i></i></span></div>
    <div class="q-head"></div>
    <p class="q-kicker">FIRE RISK ASSESSMENT</p>
    <p class="q-title">Fire Hazards</p>
    <p class="q-section">Section <b>22.5</b> / 30.00</p>
    <div class="q-save"><i></i>Save and close</div>
    <div class="q-body">
      <span class="badge-ico"><svg width="12" height="14" viewBox="0 0 12 14"><polygon points="7,0 1,8 5,8 4,14 11,5 7,5" fill="#f0912c"/></svg></span>
      <p class="center-t q-topic" style="top:16px">Electronic Sources of Ignition</p>
      <p class="center-t q-clause" style="top:25px">(Clause 13 &amp; Annex B)</p>
      <p class="q-num" style="top:54px">QUESTION 22.05</p>
      <p class="q-text" style="top:62px">Are reasonable measures taken to prevent fires of electrical origin?</p>
      <div class="answers" style="top:92px"><span class="ans no sel"><i>✕</i>No</span><span class="ans na"><i>⊘</i>N/A</span><span class="ans yes"><i>✓</i>Yes</span></div>
      <div class="comment" style="top:126px">No, electric sockets are overloaded.</div>
      <p class="mini" style="top:149px">MORE OPTIONS</p>
      <div class="tools" style="top:158px"><span class="tool"><i></i>Mic</span><span class="tool"><i></i>Take a photo</span></div>
      <p class="mini" style="top:182px">PHOTOS</p>
      <div class="photo" role="img" aria-label="Photo of overloaded electrical sockets and cables"><span class="remove"></span></div>
      <div class="progress" style="top:368px"><div class="meta"><span>ASSESSMENT PROGRESS</span><span>60%</span></div><div class="bar"><i></i></div></div>
      <div class="nav" style="top:388px"><span class="pill line">← Prev</span><span class="pill solid">Next →</span></div>
    </div>
    <span class="home-bar dark"></span>
  </section>

  <!-- Row 4 -->
  <span class="label" style="left:549px;top:1684px">ADD ASSESSMENT - QUESTION</span>
  <section class="screen" style="left:568px;top:1478px">
    <div class="status"><span>9:41</span><span><i></i><i></i><i></i></span></div>
    <div class="q-head"></div>
    <p class="q-kicker">FIRE RISK ASSESSMENT</p>
    <p class="q-title">Fire Hazards</p>
    <p class="q-section">Section <b>22.5</b> / 30.00</p>
    <div class="q-save"><i></i>Save and close</div>
    <div class="q-body">
      <span class="badge-ico"><svg width="12" height="14" viewBox="0 0 12 14"><polygon points="7,0 1,8 5,8 4,14 11,5 7,5" fill="#f0912c"/></svg></span>
      <p class="center-t q-topic" style="top:16px">Electronic Sources of Ignition</p>
      <p class="center-t q-clause" style="top:25px">(Clause 13 &amp; Annex B)</p>
      <p class="q-num" style="top:54px">QUESTION 22.05</p>
      <p class="q-text" style="top:62px">Are reasonable measures taken to prevent fires of electrical origin?</p>
      <div class="answers" style="top:92px"><span class="ans no"><i>✕</i>No</span><span class="ans na"><i>⊘</i>N/A</span><span class="ans yes"><i>✓</i>Yes</span></div>
      <p class="mini" style="top:144px">MORE OPTIONS</p>
      <div class="tools" style="top:154px"><span class="tool"><i></i>Mic</span><span class="tool"><i></i>Take a photo</span></div>
      <div class="progress" style="top:196px"><div class="meta"><span>ASSESSMENT PROGRESS</span><span>60%</span></div><div class="bar"><i></i></div></div>
      <div class="nav" style="top:216px"><span class="pill line">← Prev</span><span class="pill solid">Next →</span></div>
    </div>
    <span class="home-bar dark"></span>
  </section>

  <span class="label" style="left:772px;top:1728px">ADD ASSESSMENT - QUESTION - YES</span>
  <section class="screen" style="left:791px;top:1478px">
    <div class="status"><span>9:41</span><span><i></i><i></i><i></i></span></div>
    <div class="q-head"></div>
    <p class="q-kicker">FIRE RISK ASSESSMENT</p>
    <p class="q-title">Fire Hazards</p>
    <p class="q-section">Section <b>22.5</b> / 30.00</p>
    <div class="q-save"><i></i>Save and close</div>
    <div class="q-body">
      <span class="badge-ico"><svg width="12" height="14" viewBox="0 0 12 14"><polygon points="7,0 1,8 5,8 4,14 11,5 7,5" fill="#f0912c"/></svg></span>
      <p class="center-t q-topic" style="top:16px">Electronic Sources of Ignition</p>
      <p class="center-t q-clause" style="top:25px">(Clause 13 &amp; Annex B)</p>
      <p class="q-num" style="top:54px">QUESTION 22.05</p>
      <p class="q-text" style="top:62px">Are reasonable measures taken to prevent fires of electrical origin?</p>
      <div class="answers" style="top:92px"><span class="ans no"><i>✕</i>No</span><span class="ans na"><i>⊘</i>N/A</span><span class="ans yes sel"><i>✓</i>Yes</span></div>
      <p class="mini" style="top:144px">MORE OPTIONS</p>
      <div class="tools" style="top:154px"><span class="tool"><i></i>Mic</span><span class="tool"><i></i>Take a photo</span></div>
      <div class="progress" style="top:196px"><div class="meta"><span>ASSESSMENT PROGRESS</span><span>60%</span></div><div class="bar"><i></i></div></div>
      <div class="nav" style="top:216px"><span class="pill line">← Prev</span><span class="pill solid">Next →</span></div>
    </div>
    <span class="home-bar dark"></span>
  </section>

  <span class="label" style="left:995px;top:1720px">ADD ASSESSMENT - QUESTION - NO</span>
  <section class="screen" style="left:1014px;top:1478px">
    <div class="status"><span>9:41</span><span><i></i><i></i><i></i></span></div>
    <div class="q-head"></div>
    <p class="q-kicker">FIRE RISK ASSESSMENT</p>
    <p class="q-title">Fire Hazards</p>
    <p class="q-section">Section <b>22.5</b> / 30.00</p>
    <div class="q-save"><i></i>Save and close</div>
    <div class="q-body">
      <span class="badge-ico"><svg width="12" height="14" viewBox="0 0 12 14"><polygon points="7,0 1,8 5,8 4,14 11,5 7,5" fill="#f0912c"/></svg></span>
      <p class="center-t q-topic" style="top:16px">Electronic Sources of Ignition</p>
      <p class="center-t q-clause" style="top:25px">(Clause 13 &amp; Annex B)</p>
      <p class="q-num" style="top:54px">QUESTION 22.05</p>
      <p class="q-text" style="top:62px">Are reasonable measures taken to prevent fires of electrical origin?</p>
      <div class="answers" style="top:92px"><span class="ans no sel"><i>✕</i>No</span><span class="ans na"><i>⊘</i>N/A</span><span class="ans yes"><i>✓</i>Yes</span></div>
      <div class="comment" style="top:126px">No, electric sockets are overloaded.</div>
      <p class="mini" style="top:164px">MORE OPTIONS</p>
      <div class="tools" style="top:174px"><span class="tool"><i></i>Mic</span><span class="tool"><i></i>Take a photo</span></div>
      <div class="progress" style="top:196px"><div class="meta"><span>ASSESSMENT PROGRESS</span><span>60%</span></div><div class="bar"><i></i></div></div>
      <div class="nav" style="top:216px"><span class="pill line">← Prev</span><span class="pill solid">Next →</span></div>
    </div>
    <span class="home-bar dark"></span>
  </section>

</main>
</body>
</html>
```